Brightmere Realty information card

We need a 5x7 two-sided card to hand out at open houses and provide to our charitable partners for distribution. We are a local real estate group looking to add a "give back" component to our business. We are located in a coastal community and would like to incorporate that feel into our design. We are giving clients who use us the ability to designate 1 out of the 10 charitable organizations we partner with - and we will make a donation to that organization.

We included the 10 partner logos below - we envision them pretty small. Also included 2 photos of the "Brightmere" and our logo. Have fun.
Updates

Project Deadline Extended
Reason: We're out of town until Wednesday, May 17th.

Target Market(s)

home buyers & sellers

Industry/Entity Type

Real Estate

Font styles to use
Serif
Sans Serif

Colors

Designer to choose colors to be used in the design.

Requirements
Must have
• slogan & tagline - see attached text file
• Brightmere photo
Nice to have
• partner logos - small - maybe in circles?

```html
<!DOCTYPE html>
<html lang="en">
<head>
<meta charset="utf-8">
<title>Brightmere Realty – Give Back Card</title>
<link href="https://fonts.googleapis.com/css2?family=Bebas+Neue&family=Yanone+Kaffeesatz:wght@500&family=Delius&family=Ubuntu:wght@400;500&display=swap" rel="stylesheet">
<style>
  :root{
    --canvas:#c9c9c9;
    --ink:#000;
    --white:#fff;
    --link:#8fb4ff;
    --accent:#4a8cf0;
    --sky-top:#6f7c9c;
    --sky-pink:#e58a86;
    --sky-orange:#f3a279;
    --sea:#d98a78;
    --city:#3a3440;
    --city-dark:#221e27;
    --veil:rgba(40,36,48,.45);
  }
  *{box-sizing:border-box;margin:0;padding:0}
  html,body{width:1200px;height:1200px;overflow:hidden;background:var(--canvas)}
  .card{position:absolute;width:730px;height:520px;background:var(--ink);overflow:hidden;box-shadow:6px 8px 8px rgba(0,0,0,.35)}
  .card--front{left:150px;top:50px}
  .card--back{left:375px;top:630px}

  .photo{position:absolute;left:0;right:0;
    background:linear-gradient(180deg,var(--sky-top) 0%,#9a8ea8 14%,var(--sky-pink) 32%,var(--sky-orange) 48%,var(--sea) 58%,#6d5560 66%,var(--city) 78%,var(--city-dark) 100%)}
  .card--front .photo{top:50px;bottom:46px}
  .card--back .photo{top:22px;bottom:52px}

  .brand-tab{position:absolute;left:50%;top:0;transform:translateX(-50%);width:184px;height:100px}
  .brand-tab svg{position:absolute;inset:0}
  .brand-name{position:absolute;left:0;right:0;top:26px;text-align:center;font-family:"Ubuntu",sans-serif;font-weight:500;color:var(--white);font-size:18px;line-height:1.05}
  .brand-name span{display:block;font-size:15px}

  .headline{position:absolute;left:0;right:0;text-align:center;font-family:"Bebas Neue",sans-serif;color:var(--white);text-shadow:2px 3px 3px rgba(0,0,0,.55);letter-spacing:.5px;white-space:nowrap}
  .card--front .headline{top:148px;font-size:74px;line-height:1}
  .card--back .headline{top:60px;font-size:46px;line-height:1}

  .tagline{position:absolute;left:0;right:0;top:225px;text-align:center;font-family:"Yanone Kaffeesatz",sans-serif;font-weight:500;font-size:30px;color:var(--white);text-shadow:1px 2px 2px rgba(0,0,0,.5)}

  .veil{position:absolute;left:0;right:0;background:var(--veil);font-family:"Delius",cursive;color:var(--white);text-align:center}
  .card--front .veil{top:355px;height:100px;padding:10px 18px;font-size:15.5px;line-height:1.5}
  .card--back .veil{top:215px;height:130px;padding:14px 70px;font-size:12.5px;line-height:1.5}
  .veil p+p{margin-top:10px}

  .intro{position:absolute;left:0;right:0;top:125px;text-align:center;font-family:"Delius",cursive;font-size:14px;line-height:1.45;color:var(--ink)}

  .contact-bar{position:absolute;left:0;right:0;bottom:0;height:46px;display:flex;align-items:center;justify-content:space-between;padding:0 22px 0 26px;font-family:"Ubuntu",sans-serif;font-size:11.5px;color:var(--white);white-space:nowrap}
  .contact{display:flex;align-items:baseline;gap:10px}
  .contact a{color:var(--link);text-decoration:none}
  .contact-bar .site{color:var(--link);text-decoration:none;font-size:13.5px}

  .partners{position:absolute;left:30px;right:20px;top:390px;display:flex;justify-content:space-between;align-items:center}
  .partner{width:56px;height:56px;border-radius:50%;border:2px solid #8fa8e0;background:var(--white)}
  .partner--slate{background:#7d7f8c}
  .partner--hill{background:#5c7a5a}
  .partner--earth{background:#6b5a4c}
  .partner--navy{background:#152646;border-color:var(--accent)}
  .partner--pink{background:#e68ac6}
  .partner--black{background:#111;border-color:#ddd}
  .partner--red{background:#c8172a}
</style>
</head>
<body>

<section class="card card--front">
  <div class="photo" role="img" aria-label="Sunset over the coastal bay and town, seen from a hillside"></div>
  <div class="brand-tab">
    <svg viewBox="0 0 184 100" aria-hidden="true"><polygon points="0,0 184,0 92,100" fill="#000"/></svg>
    <div class="brand-name">Brightmere<span>Realty</span></div>
  </div>
  <h1 class="headline">Change Homes, Change Lives</h1>
  <p class="tagline">Changing the World One Home at a Time</p>
  <div class="veil">
    <p>Because we value generosity and desire to make a difference in our community and world, for every home bought or sold through us, we will make a contribution to one of our amazing partner who are helping to change the world.</p>
  </div>
  <footer class="contact-bar">
    <div class="contact"><span>Owen Hartley</span><a href="#">owen@brightmererealty.com</a></div>
    <a class="site" href="#">www.brightmererealty.com</a>
    <div class="contact"><a href="#">clara@brightmererealty.com</a><span>Clara Hartley</span></div>
  </footer>
</section>

<section class="card card--back">
  <div class="photo" role="img" aria-label="Sunset sky over the coastal town at dusk"></div>
  <h2 class="headline">We Live Here. &nbsp;We Give Here.</h2>
  <p class="intro">We give because we value generosity and believe we have been blessed to be a blessing.<br>We believe that together we can change the world one home at time.</p>
  <div class="veil">
    <p>You have our guarantee of personal service and no additional costs. The donations come out of our commission, not your pocket. You get to designate which of our amazing partner organizations you would like us to contribute to on behalf of your transaction.</p>
    <p>When you are ready to buy or sell, please consider giving us a call. Tell a friend about us too. Together, we can make the world a better place.</p>
  </div>
  <div class="partners" aria-label="Partner organizations">
    <span class="partner partner--slate"></span>
    <span class="partner"></span>
    <span class="partner partner--hill"></span>
    <span class="partner partner--earth"></span>
    <span class="partner partner--navy"></span>
    <span class="partner partner--pink"></span>
    <span class="partner partner--black"></span>
    <span class="partner"></span>
    <span class="partner partner--red"></span>
    <span class="partner"></span>
  </div>
</section>

</body>
</html>
```